Pinpoint Buried Network Services
Thank you all for submitting designs. You guys make it really tough to pick a design they were all good.
Thanks again.
I just added more funds to the project. I will need a word template for the letterhead.
I do not need any business card designs they are all good. Just looking at matching stationery now.
Thank you.
Please include a matching letterhead. I will add more funds to the project for stationery.
Could you include stationery.
I have attached our logo and sample biz card front and back.
Use tag line in front and list of service in back of card.
Only use contact information in the brief.

```html
<!DOCTYPE html>
<html lang="en">
<head>
<meta charset="utf-8">
<title>Pinpoint Buried Network Services – Stationery</title>
<link rel="stylesheet" href="https://fonts.googleapis.com/css2?family=Open+Sans:wght@400;700&display=swap">
<style>
:root{
  --bg:#5b3f2a;
  --paper:#ffffff;
  --paper-shade:#eeeeee;
  --gold:#f5b21b;
  --ink:#1e1e1e;
  --ink-soft:#555555;
  --label:#e8dccd;
  --fold:#d4d4d4;
}
*{box-sizing:border-box;margin:0;padding:0}
html,body{width:1200px;height:343px;overflow:hidden}
body{background:var(--bg);font-family:"Open Sans",Arial,sans-serif;color:var(--ink);position:relative}
.sheet{position:absolute;background:var(--paper);box-shadow:0 2px 5px rgba(0,0,0,.35);overflow:hidden}
.label{position:absolute;font-size:5px;color:var(--label);text-align:center}
.mark{display:flex;align-items:center;gap:3px;font-weight:700;color:var(--ink);line-height:1.1}
.mark .dot{flex:none;border-radius:50%;background:var(--gold)}
.corner{position:absolute}
.tiny{font-size:4px;line-height:1.35;color:var(--ink-soft)}
.watermark{position:absolute;left:0;right:0;text-align:center;font-weight:700;color:var(--ink);opacity:.06;line-height:1.05}

/* business cards */
.card{width:92px;height:60px;left:24px}
.card .mark{position:absolute;left:6px;top:8px;width:42px;font-size:5px}
.card .mark .dot{width:8px;height:8px}
.card .info{position:absolute;left:50px;top:24px;width:40px}
.card .info .person{display:block;font-size:5px;font-weight:700;color:var(--ink);line-height:1.3}
.card .list{position:absolute;left:50px;top:10px;list-style:none}
.card .list li{font-size:4px;color:var(--ink-soft);line-height:1.5}
.card .list li::before{content:"";display:inline-block;width:3px;height:3px;background:var(--gold);margin-right:2px;vertical-align:middle}
.card.alt{background:var(--gold)}
.card.alt .list li{color:var(--ink)}
.card.alt .list li::before{background:var(--ink)}

/* letterheads */
.letterhead{top:19px;width:192px;height:292px}
.letterhead .mark{position:absolute;font-size:6px}
.letterhead .mark .dot{width:10px;height:10px}
.letterhead .contact{position:absolute}
.letterhead .footer{position:absolute;bottom:12px;left:0;right:0;text-align:center}

/* envelopes */
.envelope .mark{position:absolute;font-size:5px}
.envelope .mark .dot{width:8px;height:8px}
.flap{position:absolute;left:0;top:0;width:100%}
</style>
</head>
<body>

<!-- business card: front -->
<div class="sheet card" style="top:41px">
  <svg class="corner" style="right:0;top:0" width="18" height="18" viewBox="0 0 18 18"><polygon points="0,0 18,0 18,18" fill="var(--gold)"/></svg>
  <div class="mark"><span class="dot"></span>Pinpoint Buried Network Services</div>
  <div class="info tiny">
    <span class="person">tmacphee</span>Project Manager<br>555 014 2290<br>mail@pinpointbns.com
  </div>
  <div class="tiny" style="position:absolute;left:6px;bottom:6px">Locate Before You Dig</div>
</div>
<div class="label" style="left:24px;top:104px;width:92px">Card front</div>

<!-- business card: back -->
<div class="sheet card" style="top:137px">
  <svg class="corner" style="left:0;bottom:0" width="18" height="18" viewBox="0 0 18 18"><polygon points="0,0 0,18 18,18" fill="var(--gold)"/></svg>
  <div class="mark"><span class="dot"></span>Pinpoint Buried Network Services</div>
  <ul class="list"><li>Utility Locating</li><li>GPR Scanning</li><li>Video Inspection</li><li>Site Mapping</li></ul>
</div>
<div class="label" style="left:24px;top:200px;width:92px">Card back</div>

<!-- business card: alternate -->
<div class="sheet card alt" style="top:233px">
  <div class="mark" style="top:18px"><span class="dot" style="background:var(--paper)"></span>Pinpoint Buried Network Services</div>
  <ul class="list"><li>Utility Locating</li><li>GPR Scanning</li><li>Video Inspection</li><li>Site Mapping</li></ul>
</div>
<div class="label" style="left:24px;top:296px;width:92px">Card alternate</div>

<!-- letterhead one -->
<div class="sheet letterhead" style="left:173px">
  <svg class="corner" style="right:0;top:0" width="30" height="30" viewBox="0 0 30 30"><polygon points="0,0 30,0 30,30" fill="var(--gold)"/></svg>
  <svg class="corner" style="left:0;bottom:0" width="20" height="20" viewBox="0 0 20 20"><polygon points="0,0 0,20 20,20" fill="var(--gold)"/></svg>
  <div class="mark" style="left:58px;top:12px;width:62px"><span class="dot"></span>Pinpoint Buried Network Services</div>
  <div class="contact tiny" style="left:122px;top:9px">14 Quarry Lane<br>Ashford, ON<br>555 014 2290<br>pinpointbns.com</div>
  <div class="watermark" style="top:110px;font-size:20px">Pinpoint Buried<br>Network Services</div>
  <div class="footer tiny">14 Quarry Lane · Ashford · 555 014 2290 · pinpointbns.com</div>
</div>

<!-- letterhead two -->
<div class="sheet letterhead" style="left:389px">
  <svg class="corner" style="right:0;top:0" width="20" height="20" viewBox="0 0 20 20"><polygon points="0,0 20,0 20,20" fill="var(--gold)"/></svg>
  <svg class="corner" style="left:0;bottom:0" width="20" height="20" viewBox="0 0 20 20"><polygon points="0,0 0,20 20,20" fill="var(--gold)"/></svg>
  <div class="mark" style="left:66px;top:12px;width:62px"><span class="dot"></span>Pinpoint Buried Network Services</div>
  <div class="watermark" style="top:110px;font-size:20px">Pinpoint Buried<br>Network Services</div>
  <div class="footer tiny">14 Quarry Lane · Ashford · 555 014 2290 · pinpointbns.com</div>
</div>

<!-- envelope small -->
<div class="sheet envelope" style="left:636px;top:67px;width:156px;height:101px">
  <svg class="corner" style="left:0;top:0" width="18" height="18" viewBox="0 0 18 18"><polygon points="0,0 18,0 0,18" fill="var(--gold)"/></svg>
  <div class="mark" style="left:12px;top:10px;width:52px"><span class="dot"></span>Pinpoint Buried Network Services</div>
  <div class="tiny" style="position:absolute;left:12px;top:30px">14 Quarry Lane Ashford ON</div>
  <div class="watermark" style="top:42px;font-size:11px">Pinpoint Buried Network Services</div>
</div>
<div class="label" style="left:636px;top:172px;width:156px">Envelope</div>

<!-- envelope large -->
<div class="sheet envelope" style="left:643px;top:204px;width:266px;height:89px">
  <svg class="corner" style="left:0;top:0" width="18" height="18" viewBox="0 0 18 18"><polygon points="0,0 18,0 0,18" fill="var(--gold)"/></svg>
  <div class="mark" style="left:12px;top:10px;width:56px"><span class="dot"></span>Pinpoint Buried Network Services</div>
  <div class="tiny" style="position:absolute;left:12px;top:30px">14 Quarry Lane Ashford ON</div>
  <div class="watermark" style="top:38px;font-size:14px">Pinpoint Buried Network Services</div>
</div>
<div class="label" style="left:643px;top:297px;width:266px">Envelope large</div>

<!-- envelope backs: black flap -->
<div class="sheet envelope" style="left:941px;top:67px;width:252px;height:100px;background:var(--paper-shade)">
  <svg class="flap" height="60" viewBox="0 0 252 60" preserveAspectRatio="none"><polygon points="0,0 252,0 126,60" fill="var(--ink)"/></svg>
  <div class="mark" style="left:100px;top:14px;width:60px;color:var(--paper)"><span class="dot"></span>Pinpoint Buried Network Services</div>
</div>

<!-- envelope backs: gold flap -->
<div class="sheet envelope" style="left:912px;top:124px;width:262px;height:104px;background:var(--paper-shade)">
  <svg class="flap" height="62" viewBox="0 0 262 62" preserveAspectRatio="none"><polygon points="0,0 262,0 131,62" fill="var(--gold)"/></svg>
  <div class="mark" style="left:104px;top:16px;width:60px"><span class="dot" style="background:var(--ink)"></span>Pinpoint Buried Network Services</div>
</div>

<!-- envelope backs: white flap -->
<div class="sheet envelope" style="left:924px;top:192px;width:252px;height:101px">
  <svg class="flap" height="101" viewBox="0 0 252 101" preserveAspectRatio="none">
    <polyline points="0,0 126,58 252,0" fill="none" stroke="var(--fold)" stroke-width="1"/>
    <polyline points="0,101 126,48 252,101" fill="none" stroke="var(--paper-shade)" stroke-width="1"/>
  </svg>
  <div class="mark" style="left:100px;top:14px;width:60px"><span class="dot"></span>Pinpoint Buried Network Services</div>
</div>

</body>
</html>
```